Quellmont Home Roadmap for Street Safety

We need to re-work our "Home Roadmap for Street Safety" brochures (English & Spanish) to give it greater visual appeal with updated photos and graphics; the content (text) is currently being edited, but is not expected to be drastically different. It's important that we uses images and graphics that strike a delicate balance between conveying the image of gangs or gang members without glorifying gangs or portraying the City or even a particular race in bad light. Abstract, silhouette, faceless, and ambiguous images are preferred. Other images portraying kids or families should be diverse (white, African-American, Latino, Asian, etc.) and inclusive of both males and females. The design should communicate that help and resources are available. Please see attachments for current brochure designs in Spanish and English.

Target Market(s)

Parents of gang members, gang-associates, and other at-risk youth

Industry/Entity Type

Work

Font styles to use
Serif

Requirements
Must have
• City of Quellmont logo. We''re flexible on the size... could be 8.5" x 14" folded to a 4-panel, 2-sided brochure, or could simply be 8.5'' x 11" folded in half. The current brochure design can give you an idea of the space required for the content.
Nice to have
• Some images that might covey the idea of police interaction such as a silhouette or no-face image from behind gang members or police officers and police cars in dark alley. Also, positive images of Oxnard scenes or families and non-gang kids (boys & girls) of various ethnicities (white, African-American, Latino, Asian) .
Should not have
• Images that may be perceived negatively such as bloody crime scenes, officers using guns, batons, or handcuffs, or images that glorify the gang lifestyle

```html
<!DOCTYPE html>
<html lang="en">
<head>
<meta charset="utf-8">
<title>Quellmont Home Roadmap for Street Safety</title>
<link href="https://fonts.googleapis.com/css2?family=PT+Serif:ital,wght@0,400;0,700;1,400;1,700&family=Playfair+Display:wght@400;700;800;900&display=swap" rel="stylesheet">
<style>
  :root {
    --navy: #1d3f8f;
    --deep-blue: #12306e;
    --royal: #2450a8;
    --orange: #f2a21b;
    --ink: #1b1b1b;
    --white: #ffffff;
    --brick-dark: #5e4a44;
    --brick-mid: #8a7268;
  }
  * { box-sizing: border-box; margin: 0; padding: 0; }
  html, body { width: 1200px; height: 733px; overflow: hidden; background: var(--white); }
  body { font-family: "PT Serif", Georgia, serif; color: var(--ink); }

  .brochure { position: relative; width: 1200px; height: 733px; overflow: hidden; background: var(--white); }

  .brick-wall {
    position: absolute; left: 0; top: 0; width: 584px; height: 733px;
    background: linear-gradient(135deg, #7d665d 0%, var(--brick-mid) 35%, #9c8a80 55%, var(--brick-dark) 100%);
  }

  /* Panel 1 — message to parents */
  .panel-message {
    position: absolute; left: 7px; top: 18px; width: 268px; height: 702px;
    background: var(--white); border-radius: 14px; overflow: hidden;
  }
  .family-photo {
    height: 218px; width: 100%; position: relative;
    background: linear-gradient(160deg, #cfe3a6 0%, #a9c67a 40%, #7a8f55 100%);
  }
  .photo-caption { position: absolute; left: 6px; bottom: 4px; font-size: 5px; color: var(--white); }
  .panel-message .body { padding: 10px 14px 0 16px; }
  .section-title {
    font-family: "Playfair Display", Georgia, serif; font-style: italic; font-weight: 700;
    color: var(--navy); font-size: 15px; line-height: 1.15; margin-bottom: 4px;
  }
  .copy { font-size: 10.5px; line-height: 1.25; margin-bottom: 6px; }

  .city-mark { display: flex; align-items: center; gap: 8px; }
  .city-mark .dot { width: 12px; height: 12px; border-radius: 50%; background: var(--orange); flex: none; }
  .city-mark .name { font-family: "PT Serif", Georgia, serif; font-weight: 700; color: var(--navy); font-size: 18px; white-space: nowrap; }
  .panel-message .city-mark { position: absolute; left: 30px; top: 596px; }

  /* Panel 2 — warning signs */
  .panel-behaviors {
    position: absolute; left: 289px; top: 0; width: 295px; height: 733px;
    background: rgba(255,255,255,0.9); padding: 34px 13px 0 14px;
  }
  .behavior-list { list-style: none; margin: 2px 0 3px; }
  .behavior-list li { position: relative; padding-left: 18px; font-size: 10.5px; line-height: 1.22; margin-bottom: 2px; }
  .behavior-list li::before {
    content: ""; position: absolute; left: 5px; top: 3px;
    border-left: 6px solid var(--orange); border-top: 4px solid transparent; border-bottom: 4px solid transparent;
  }
  .sign { font-size: 10.5px; line-height: 1.22; margin-bottom: 2px; }
  .sign strong { color: var(--royal); font-weight: 700; }

  /* Panel 3 — resources */
  .panel-resources {
    position: absolute; left: 584px; top: 0; width: 301px; height: 733px; padding: 16px 12px 0 10px;
    background: linear-gradient(90deg, var(--white) 0%, var(--white) 82%, #eef0f5 100%);
  }
  .resources-title { font-family: "Playfair Display", Georgia, serif; font-weight: 700; color: var(--navy); font-size: 14.5px; line-height: 1.1; }
  .report-title { color: var(--orange); font-weight: 700; font-size: 11px; margin-top: 2px; }
  .resource-line { font-size: 10.5px; line-height: 1.28; margin-bottom: 2px; }
  .resource-gap { margin-top: 12px; }
  .resource-strong { font-weight: 700; font-size: 10.5px; line-height: 1.25; }
  .web-link { color: var(--royal); font-weight: 700; }
  .kids-circle {
    position: absolute; left: 30px; top: 378px; width: 192px; height: 192px; border-radius: 50%;
    border: 9px solid var(--orange);
    background: radial-gradient(circle at 50% 55%, #d9b08c 0%, #c9c4c6 40%, #a9c6e6 70%, #8fb1d8 100%);
  }
  .funding-note { position: absolute; left: 6px; top: 608px; width: 290px; font-size: 8.4px; line-height: 1.2; }

  /* Panel 4 — cover */
  .panel-cover { position: absolute; left: 885px; top: 0; width: 315px; height: 733px; background: var(--white); }
  .cover-scene {
    position: absolute; left: 0; top: 0; width: 315px; height: 580px;
    background:
      radial-gradient(ellipse 60% 22% at 78% 12%, rgba(150,190,255,0.55) 0%, rgba(150,190,255,0) 100%),
      linear-gradient(180deg, rgba(8,22,60,0.75) 0%, rgba(8,22,60,0) 28%),
      radial-gradient(ellipse 70% 30% at 55% 52%, rgba(110,150,220,0.45) 0%, rgba(110,150,220,0) 100%),
      linear-gradient(180deg, #1a3d86 0%, #2a58ad 45%, #1c418f 70%, #0f2a66 100%);
  }
  .cover-title { position: absolute; left: 0; top: 388px; width: 315px; text-align: center; color: var(--white); font-weight: 400; }
  .cover-title .kicker { display: block; font-family: "Playfair Display", Georgia, serif; font-weight: 400; color: var(--orange); font-size: 20px; letter-spacing: 2.5px; line-height: 1.1; }
  .cover-title .main { display: block; font-family: "Playfair Display", Georgia, serif; font-weight: 900; font-size: 32px; line-height: 1.1; letter-spacing: 0.5px; }
  .cover-tagline { position: absolute; left: 38px; top: 496px; width: 240px; text-align: center; color: var(--white); font-size: 10.5px; line-height: 1.3; font-weight: 700; }
  .panel-cover .city-mark { position: absolute; left: 44px; top: 616px; }
  .panel-cover .city-mark .name { font-size: 22px; }
</style>
</head>
<body>
<main class="brochure">
  <div class="brick-wall" role="img" aria-label="Painted brick wall background"></div>

  <section class="panel-message">
    <div class="family-photo" role="img" aria-label="Photo of a smiling family of three posing outdoors">
      <span class="photo-caption">Posed by models.</span>
    </div>
    <div class="body">
      <h2 class="section-title">A Message to Parents</h2>
      <p class="copy">Research indicates that you, as a parent, play a vital role in keeping your child out of gangs. Negative influences within the family—including domestic violence, child abuse, harsh or inconsistent parenting practices, and/or drug/alcohol abuse by family members—can increase the risk that your child will join a gang.</p>
      <p class="copy">You can protect your child from gang activity through taking positive actions, such as monitoring your children's activities, maintaining a close relationship with them, and using positive discipline strategies. This brochure contains information about gangs and what you, as a parent, can do to help your child avoid them.</p>
    </div>
    <div class="city-mark"><span class="dot"></span><span class="name">City of Quellmont</span></div>
  </section>

  <section class="panel-behaviors">
    <h2 class="section-title">Behaviors Associated With Joining a Gang</h2>
    <p class="copy">The early adolescent years (12–14 years of age) are a crucial time when youths are exposed to gangs and may consider joining a gang. Youths who are becoming involved in a gang may exhibit the following behaviors:</p>
    <p class="sign">Negative changes in behavior, such as:</p>
    <ul class="behavior-list">
      <li>Declining school attendance, performance, or behavior.</li>
      <li>Staying out late without reason.</li>
      <li>Unusual desire for secrecy.</li>
      <li>Confrontational behavior, such as talking back, verbal abuse, name calling, and disrespect for parental authority.</li>
      <li>Sudden negative opinions about law enforcement or adults in positions of authority (school officials or teachers).</li>
      <li>Change in attitude about school, church, or other normal activities or change in behavior at these activities.</li>
    </ul>
    <p class="sign"><strong>Unexplained cash or goods,</strong> such as clothing or jewelry.</p>
    <p class="sign"><strong>Unusual interest in a particular type of clothing or a particular logo.</strong></p>
    <p class="sign"><strong>Use and practice of hand signals to communicate with friends.</strong></p>
    <p class="sign"><strong>Peculiar drawings or gang symbols on schoolbooks, clothing, notebooks, or even walls.</strong></p>
    <p class="sign"><strong>Drastic changes in hair or dress style</strong> and/or having a group of friends who have the same hair or dress style.</p>
    <p class="sign"><strong>Withdrawal from long time friends</strong> and forming bonds with an entirely new group of friends.</p>
    <p class="sign"><strong>Suspected drug use,</strong> such as alcohol, inhalants, and narcotics.</p>
    <p class="sign"><strong>The presence of firearms,</strong> ammunition, or other weapons.</p>
    <p class="sign"><strong>Non-accidental physical injuries,</strong> such as being beaten or injuries to hands and knuckles from fighting.</p>
    <p class="sign"><strong>Interest in gang-influenced music, videos, and movies</strong></p>
  </section>

  <section class="panel-resources">
    <h2 class="resources-title">Additional Resources and Information:</h2>
    <p class="report-title">To Report Gang Activity</p>
    <p class="resource-line">Emergencies call 9-1-1</p>
    <p class="resource-line">Non-emergency call 555-0143</p>
    <p class="resource-line">Involving your child in positive youth development activities is a good way to keep them away from negative people and behavior. The programs listed below offer a variety of positive activities.</p>
    <p class="resource-line">City Corps call 555-0181</p>
    <p class="resource-line">PAL (Police Activities League) call 555-0130</p>
    <p class="resource-line">Recreation Department call 555-0195</p>
    <p class="resource-line">Other Community Programs call 2-1-1</p>
    <p class="resource-line resource-gap">To learn more about gang indicators, how to get help for your child and family, and other programs and activities in the community visit <span class="web-link">www.SaferStreetsQuellmont.org</span></p>
    <p class="resource-strong">If you have questions about your child's possible involvement in gangs, call the Gang Reduction Coordinator at 555-0190.</p>
    <div class="kids-circle" role="img" aria-label="Circular photo of a diverse group of kids huddled together, seen from below"></div>
    <p class="funding-note">This project was supported by funding granted under the State Youth Safety &amp; Prevention (SYSP) Program awarded through the State Office of Emergency Services (SOES). Some content provided by the Federal Office for Youth Justice, Federal Justice Agency. Points of view in this publication are those of the City of Quellmont and do not necessarily represent the official position or policies of the Federal Justice Agency.</p>
  </section>

  <section class="panel-cover">
    <div class="cover-scene" role="img" aria-label="Blue-toned photo of faceless figures walking away down a tree-lined street at dusk"></div>
    <h1 class="cover-title">
      <span class="kicker">Home Roadmap for</span>
      <span class="main">STREET SAFETY</span>
    </h1>
    <p class="cover-tagline">This guide is designed to provide parents with information in order to recognize and prevent gang involvement.</p>
    <div class="city-mark"><span class="dot"></span><span class="name">City of Quellmont</span></div>
  </section>
</main>
</body>
</html>
```